Business card design for IT consulting company

Looking for a simple, modern, clean business card design.
Open to reworking our existing logo.

Attached is our current business cards which we do not like.
Ideally double sided with something simple on the back.
Rectangle / Horizonal only.
No rounded edges on the card.
White as the dominate color is preferred.

Target Market(s)

clients, legal, oil & gas, medical, professionals

Industry/Entity Type

IT, tech, consulting

Contact Information for Business Card

Name, Title, email, phone, cell, website

Font styles to use
Sans Serif

Requirements
Must have
• Clean design
Should not have
• loud colors or unusual fonts, etc

```html
<!DOCTYPE html>
<html lang="en">
<head>
<meta charset="utf-8">
<title>Nexora Solutions – Business Card</title>
<link rel="stylesheet" href="https://fonts.googleapis.com/css2?family=Open+Sans:wght@400;600;700;800&display=swap">
<style>
  :root {
    --stage-top: #676c73;
    --stage-bottom: #8a8a8a;
    --card-black: #0b0b0b;
    --card-black-soft: #1a1a1a;
    --band-grey: #d3d1d2;
    --ink: #0a0a0a;
    --white: #ffffff;
  }
  * { box-sizing: border-box; margin: 0; padding: 0; }
  html, body { width: 1200px; height: 892px; overflow: hidden; }
  body {
    background: linear-gradient(180deg, var(--stage-top) 0%, var(--stage-bottom) 100%);
    font-family: "Open Sans", sans-serif;
    position: relative;
  }
  .card {
    position: absolute;
    top: 298px;
    width: 520px;
    height: 297px;
    overflow: hidden;
    background: var(--card-black);
  }
  .card--front { left: 50px; }
  .card--back { left: 630px; }

  .texture {
    position: absolute; inset: 0;
    background: radial-gradient(ellipse at 50% 40%, var(--card-black-soft) 0%, var(--card-black) 75%);
  }

  /* front */
  .front-header {
    position: absolute; left: 0; top: 0; width: 100%; height: 112px;
    display: flex; flex-direction: column; align-items: center; justify-content: center;
  }
  .brand { display: flex; align-items: center; gap: 8px; color: var(--white); font-weight: 700; }
  .brand-square { width: 14px; height: 14px; background: var(--white); }
  .brand-name { font-size: 20px; letter-spacing: 2px; }

  .info-band {
    position: absolute; left: 0; top: 112px; width: 100%; height: 164px;
    background: var(--band-grey);
    padding: 20px 24px;
  }
  .contact-list { list-style: none; display: flex; flex-direction: column; gap: 9px; }
  .contact-item {
    display: flex; align-items: center; gap: 8px;
    font-size: 14px; font-weight: 700; color: var(--ink);
  }
  .contact-icon { width: 20px; height: 20px; flex: none; }

  .identity {
    position: absolute; right: 28px; bottom: 18px;
    display: flex; flex-direction: column; align-items: flex-end;
  }
  .avatar-spot {
    width: 48px; height: 48px; border: 3px solid var(--ink); border-radius: 50%;
    background: var(--ink); margin-bottom: 4px;
  }
  .person-name { font-size: 26px; font-weight: 800; color: var(--ink); line-height: 1.1; }
  .person-title { font-size: 15px; font-weight: 400; color: var(--ink); letter-spacing: 0.5px; }

  /* back */
  .back-content {
    position: absolute; inset: 0;
    display: flex; align-items: center; justify-content: center;
  }
  .card--back .brand { gap: 14px; }
  .card--back .brand-square { width: 30px; height: 30px; }
  .card--back .brand-name { font-size: 34px; letter-spacing: 3px; }
</style>
</head>
<body>

<section class="card card--front" aria-label="Business card front">
  <div class="texture" role="img" aria-label="Dark faceted background texture"></div>
  <header class="front-header">
    <div class="brand">
      <span class="brand-square"></span>
      <span class="brand-name">NEXORA SOLUTIONS</span>
    </div>
  </header>
  <div class="info-band">
    <ul class="contact-list">
      <li class="contact-item">
        <svg class="contact-icon" viewBox="0 0 20 20" fill="none" stroke="#0a0a0a" stroke-width="1.4"><circle cx="10" cy="10" r="9"/><rect x="5" y="6.5" width="10" height="7"/><path d="M5 6.5l5 4 5-4"/></svg>
        daniel.reyes@nexora.ca
      </li>
      <li class="contact-item">
        <svg class="contact-icon" viewBox="0 0 20 20" fill="none" stroke="#0a0a0a" stroke-width="1.4"><circle cx="10" cy="10" r="9"/><path d="M7 5.5c-1 1-1 3 .5 5.5s3.5 4 5 3.5l1-1.5-2-1.5-1 .8c-1-.6-2-2-2.3-3l1-.7-.8-2.3z"/></svg>
        (555) 010-2480
      </li>
      <li class="contact-item">
        <svg class="contact-icon" viewBox="0 0 20 20" fill="none" stroke="#0a0a0a" stroke-width="1.2"><circle cx="10" cy="10" r="8"/><ellipse cx="10" cy="10" rx="3.5" ry="8"/><path d="M2 10h16M3.5 6h13M3.5 14h13"/></svg>
        www.nexora.ca
      </li>
      <li class="contact-item">
        <svg class="contact-icon" viewBox="0 0 20 20" fill="none" stroke="#0a0a0a" stroke-width="1.4"><circle cx="10" cy="10" r="9"/><rect x="7" y="4.5" width="6" height="11" rx="1"/><path d="M9.3 13.5h1.4"/></svg>
        (555) 014-7731
      </li>
    </ul>
    <div class="identity">
      <div class="avatar-spot" role="img" aria-label="Profile photo placeholder"></div>
      <p class="person-name">Daniel Reyes</p>
      <p class="person-title">IT Consultant</p>
    </div>
  </div>
</section>

<section class="card card--back" aria-label="Business card back">
  <div class="texture" role="img" aria-label="Dark faceted background texture"></div>
  <div class="back-content">
    <div class="brand">
      <span class="brand-square"></span>
      <span class="brand-name">NEXORA SOLUTIONS</span>
    </div>
  </div>
</section>

</body>
</html>
```